Business Landing Page for SEO Company

Need the landing page of the website designed - I will provide the copy, will need to include details of my company and the services offered, about us, testimonials, faq, etc., and all these elements will need to be arranged graphically on the page.

I want something similar to this: https://pebrovault.com/

Not in terms of color or theme or anything, but we offer a similar service and want to display similar information.

Th services we provide are:

Premium Links
Monthly Links Subscription
Link Insertions

Need to advertise them on the front page. Additionally need a place for testimonials, company details, etc.,

We already have logo for the website. Please use the attached file to insert the logo within the overal design.

Target Market(s)

SEO marketers and agencies

Number of Pages Required

1 page

```html
<!DOCTYPE html>
<html lang="en">
<head>
<meta charset="utf-8">
<title>Linkora – Link Building Services</title>
<link href="https://fonts.googleapis.com/css2?family=Montserrat:wght@400;500;600;700&display=swap" rel="stylesheet">
<style>
:root{
  --blue:#1e63dc;
  --blue-light:#3a86f2;
  --blue-deep:#0d3fb0;
  --orange:#ff8a00;
  --orange-dark:#f27300;
  --ink:#1b1b1b;
  --muted:#777c86;
  --pale:#eef1f6;
  --line:#c9d6ee;
  --white:#ffffff;
  --black:#000000;
}
*{box-sizing:border-box;margin:0;padding:0}
html,body{width:1200px;height:4819px;overflow:hidden}
body{font-family:'Montserrat',sans-serif;color:var(--ink);background:var(--white);position:relative}
.abs{position:absolute}
.heading{position:absolute;left:0;width:1200px;text-align:center;font-weight:600;font-size:31px;letter-spacing:.3px}
.heading::after{content:"";display:block;width:70px;height:3px;background:var(--orange);margin:14px auto 0}

/* header */
.site-header{position:absolute;top:0;left:0;width:1200px;height:88px;background:var(--white)}
.brand{position:absolute;left:125px;top:18px;font-weight:700;font-size:44px;color:var(--blue);letter-spacing:-1px}
.main-nav{position:absolute;right:140px;top:36px;display:flex;gap:56px;font-size:13px;font-weight:500;color:#556}
.main-nav .active{color:var(--orange)}

/* hero */
.hero{position:absolute;top:88px;left:0;width:1200px;height:710px}
.hero svg.bg{position:absolute;inset:0}
.hero-box{position:absolute;left:110px;top:169px;width:450px;height:261px;border:2px solid rgba(255,255,255,.85);padding:38px 0 0 42px;color:var(--white)}
.hero-box h1{font-weight:500;font-size:42px;line-height:1.05}
.hero-box h1 b{display:block;font-weight:600;font-size:62px}
.hero-box p{font-size:25px;margin-top:18px;font-weight:500}
.btn-hero{position:absolute;left:42px;top:236px;width:196px;height:46px;border-radius:23px;background:var(--orange);color:var(--white);font-weight:700;font-size:14px;letter-spacing:1px;display:flex;align-items:center;justify-content:center}
.hero-art{position:absolute;left:545px;top:45px;width:585px;height:520px;border-radius:30px;background:linear-gradient(150deg,#5fb2ff,#2d6fe6 55%,#1b4fcf);opacity:.75}

/* about */
.about-art{position:absolute;left:150px;top:840px;width:470px;height:450px;border-radius:20px;background:linear-gradient(140deg,#e8f1ff,#cfe0fb)}
.eyebrow{position:absolute;left:678px;top:912px;font-size:13px;font-weight:600;color:var(--blue);letter-spacing:1.5px}
.about-title{position:absolute;left:678px;top:930px;font-size:34px;font-weight:700}
.about-title::after{content:"";display:block;width:66px;height:3px;background:var(--orange);margin-top:8px}
.about-copy{position:absolute;left:678px;top:1010px;width:420px;font-size:13.5px;line-height:28px;color:var(--muted)}
.btn-outline{position:absolute;border:2px solid var(--orange);color:var(--orange);font-weight:600;display:flex;align-items:center;justify-content:center;letter-spacing:1px;background:var(--white)}
.about .btn-outline{left:680px;top:1172px;width:162px;height:40px;font-size:13px}

/* services */
.services{position:absolute;top:1357px;left:0;width:1200px;height:641px;background:linear-gradient(180deg,#2368de 0%,#1d5ed8 60%,#2b71e6 100%);overflow:hidden}
.services .glow{position:absolute;left:0;bottom:0;width:1200px;height:260px;background:radial-gradient(ellipse at 50% 100%,rgba(150,200,255,.45),rgba(255,255,255,0) 70%)}
.services .heading{color:var(--white);top:52px}
.diamond{position:absolute;width:312px;height:312px;transform:rotate(45deg)}
.diamond.orange{background:var(--orange)}
.diamond.white{background:var(--white);outline:2px solid var(--white);outline-offset:8px}
.service{position:absolute;width:260px;text-align:center;color:var(--white)}
.service .icon{width:106px;height:106px;border-radius:50%;margin:0 auto;border:3px solid var(--white);display:flex;align-items:center;justify-content:center;background:rgba(255,255,255,.12)}
.service h3{font-size:18px;font-weight:700;margin-top:18px}
.service p{font-size:12.5px;line-height:20px;margin-top:12px}
.service.dark{color:var(--ink)}
.service.dark .icon{background:var(--blue);border-color:#bcd2f5;border-width:5px}
.service.dark p{color:#555}

/* testimonials */
.testimonials .heading{top:2073px}
.t-card{position:absolute;top:2215px;width:305px;height:230px;border:2px solid #dbe6f7;text-align:center;padding:55px 30px 0}
.t-card p{font-size:13.5px;line-height:20.5px;color:var(--muted)}
.t-card h4{font-size:13px;font-weight:600;margin-top:14px}
.avatar{position:absolute;top:2177px;width:72px;height:72px;border-radius:50%;background:linear-gradient(160deg,#8a7a70,#3e3632);border:3px solid var(--white)}
.dot{position:absolute;top:2485px;width:11px;height:11px;border-radius:50%;background:#93b8ee}
.dot.on{background:var(--orange)}

/* blogs */
.blogs{position:absolute;top:2553px;left:0;width:1200px;height:650px;background:var(--pale)}
.blogs .heading{top:54px}
.blog-card{position:absolute;top:155px;width:308px;height:374px;background:var(--white);border:1px solid #dde3ec;text-align:center}
.blog-img{height:210px}
.blog-card h4{font-size:14px;font-weight:600;line-height:16px;margin:18px 30px 0}
.blog-card p{font-size:9.5px;line-height:14px;color:var(--muted);margin:12px 40px 0}
.blog-card .btn-outline{position:relative;margin:16px auto 0;width:112px;height:30px;border-radius:15px;font-size:9px}

/* faq */
.faq .heading{top:3250px;font-size:26px}
.faq-open{position:absolute;left:206px;top:3343px;width:772px;height:149px;background:var(--orange);color:var(--white);padding:26px 34px}
.faq-open h4{font-size:12.5px;font-weight:600}
.faq-open p{font-size:11.5px;line-height:21px;margin-top:14px}
.faq-item{position:absolute;left:208px;width:770px;height:50px;border:2px solid #c9cfda;padding:0 32px;display:flex;align-items:center;justify-content:space-between;font-size:11.5px;font-weight:500;color:#3f4a5c}
.chev{width:24px;height:24px}

/* contact */
.contact{position:absolute;top:3772px;left:0;width:1200px;height:670px;overflow:hidden;background:linear-gradient(180deg,#1f61da 0%,#1a56cf 60%,#0c2f7e 85%,#020a1c 100%)}
.contact .notch{position:absolute;top:0;left:0}
.contact .heading{top:168px;color:var(--white);font-size:26px}
.contact .heading::after{background:var(--white)}
.field{position:absolute;height:48px;border-radius:24px;background:var(--white);font-size:14px;padding:0 27px;display:flex;align-items:center;color:#333}
.field i{color:var(--orange);font-style:normal}
.field.msg{border-radius:14px;align-items:flex-start;padding-top:22px}
.btn-send{position:absolute;left:493px;top:540px;width:217px;height:46px;border-radius:23px;background:var(--orange);color:var(--white);font-weight:600;font-size:14px;letter-spacing:.5px;display:flex;align-items:center;justify-content:center}

/* footer */
.site-footer{position:absolute;top:4442px;left:0;width:1200px;height:377px;background:var(--black);color:var(--white)}
.site-footer .brand{left:0;width:1200px;text-align:center;top:0;color:var(--blue-light)}
.f-col{position:absolute;top:118px}
.f-col h5{font-size:15px;font-weight:600;letter-spacing:.5px;margin-bottom:18px}
.f-col li{list-style:none;font-size:11.5px;color:#bbb;line-height:33px}
.c-row{display:flex;gap:14px;margin-bottom:20px}
.c-row svg{flex:none}
.c-row b{display:block;font-size:10.5px;font-weight:700}
.c-row span{font-size:11.5px;color:#bbb}
.news-input{width:232px;height:34px;border-radius:17px;background:#2b2f39;display:flex;align-items:center;justify-content:space-between;padding:0 6px 0 20px;font-size:11px;color:#aaa}
.news-go{width:24px;height:24px;border-radius:50%;background:var(--blue-light);display:flex;align-items:center;justify-content:center}
.socials{display:flex;gap:9px;margin:30px 0 0 36px}
.socials span{width:29px;height:29px;border-radius:50%;background:var(--white)}
.socials span:first-child{background:var(--orange)}
.copy{position:absolute;right:125px;top:292px;text-align:right;font-size:11px;line-height:24px;color:#888}
</style>
</head>
<body>

<header class="site-header">
  <div class="brand">linkora</div>
  <nav class="main-nav">
    <span class="active">HOME</span><span>ABOUT US</span><span>SERVICES</span><span>TESTIMONIALS</span><span>FAQ</span><span>CONTACT</span>
  </nav>
</header>

<section class="hero">
  <svg class="bg" width="1200" height="710" viewBox="0 0 1200 710">
    <defs>
      <linearGradient id="heroGrad" x1="0" y1="0" x2="1" y2="1">
        <stop offset="0" stop-color="#2a78ec"/>
        <stop offset="1" stop-color="#1148c6"/>
      </linearGradient>
    </defs>
    <polygon points="0,0 1200,0 1200,610 600,705 0,610" fill="url(#heroGrad)"/>
    <polygon points="0,605 600,700 1200,605 1200,612 1200,640 600,712 0,640" fill="var(--orange)"/>
    <polygon points="0,640 600,712 1200,640 1200,710 0,710" fill="#fff"/>
  </svg>
  <div class="hero-art" role="img" aria-label="Isometric illustration of people working on laptops around large analytics dashboards"></div>
  <div class="hero-box">
    <h1>Welcome to<b>linkora links</b></h1>
    <p>The Real done for you link</p>
    <div class="btn-hero">LEARN MORE</div>
  </div>
</section>

<section class="about">
  <div class="about-art" role="img" aria-label="Line illustration of linked web pages and documents"></div>
  <div class="eyebrow">WHY WE ARE</div>
  <h2 class="about-title">ABOUT LINKORA</h2>
  <p class="about-copy">Lorem ipsum dolor sit amet, consectetur adipiscing elit, sed do eiusmod tempor incididunt ut labore et dolore magna aliqua. Ut enim ad minim veniam, quis nostrud exercitation ullamco laboris nisi Lorem ipsum dolor sit amet, consectetur adipiscing elit, sed do eiusmod</p>
  <div class="btn-outline">LEARN MORE</div>
</section>

<section class="services">
  <div class="glow" role="img" aria-label="Soft dotted wave pattern"></div>
  <h2 class="heading">OUR SERVICES</h2>
  <div class="diamond orange" style="left:117px;top:190px"></div>
  <div class="diamond orange" style="left:769px;top:190px"></div>
  <div class="diamond white" style="left:443px;top:190px"></div>

  <div class="service" style="left:143px;top:202px">
    <div class="icon"><svg width="46" height="40" viewBox="0 0 46 40" fill="none" stroke="#fff" stroke-width="2.5"><rect x="3" y="3" width="38" height="30" rx="3"/><line x1="3" y1="11" x2="41" y2="11"/><path d="M26 20l10 5-4 2 4 5-3 2-4-5-3 3z"/></svg></div>
    <h3>Premium Links</h3>
    <p>Lorem ipsum dolor sit amet, consectetur adipiscing elit, sed do eiusmod tempor incididunt u</p>
  </div>
  <div class="service dark" style="left:469px;top:200px">
    <div class="icon"><svg width="50" height="46" viewBox="0 0 50 46" fill="none" stroke="#fff" stroke-width="2.5"><rect x="4" y="7" width="36" height="32" rx="3"/><line x1="4" y1="15" x2="40" y2="15"/><line x1="13" y1="3" x2="13" y2="10"/><line x1="31" y1="3" x2="31" y2="10"/><circle cx="38" cy="36" r="8" fill="#1e63dc"/><path d="M34 36l3 3 5-5"/></svg></div>
    <h3>Monthly Links<br>Subscription</h3>
    <p>Lorem ipsum dolor sit amet, consectetur adipiscing elit sed</p>
  </div>
  <div class="service" style="left:795px;top:202px">
    <div class="icon"><svg width="46" height="46" viewBox="0 0 46 46" fill="none" stroke="#fff" stroke-width="3"><rect x="6" y="19" width="20" height="10" rx="5" transform="rotate(-45 16 24)"/><rect x="20" y="17" width="20" height="10" rx="5" transform="rotate(-45 30 22)"/></svg></div>
    <h3>Link Insertions</h3>
    <p>Lorem ipsum dolor sit amet, consectetur adipiscing elit, sed do eiusmod tempor incididunt ut l</p>
  </div>
</section>

<section class="testimonials">
  <h2 class="heading">TESTIMONIALS</h2>
  <div class="t-card" style="left:122px"><p>Lorem ipsum dolor sit amet, consectetur adipiscing elit, sed do eiusmod tempor incididunt ut labore et dolore magna aliqua. Ut enim ad minim veniam, quis nostrud</p><h4>OWEN HARTLEY</h4></div>
  <div class="t-card" style="left:447px"><p>Lorem ipsum dolor sit amet, consectetur adipiscing elit, sed do eiusmod tempor incididunt ut labore et dolore magna aliqua. Ut enim ad minim veniam, quis nostrud</p><h4>RHONA PELLOW</h4></div>
  <div class="t-card" style="left:770px"><p>Lorem ipsum dolor sit amet, consectetur adipiscing elit, sed do eiusmod tempor incididunt ut labore et dolore magna aliqua. Ut enim ad minim veniam, quis nostrud</p><h4>TESSA MARLOWE</h4></div>
  <div class="avatar" style="left:238px" role="img" aria-label="Portrait photo of Owen Hartley"></div>
  <div class="avatar" style="left:563px" role="img" aria-label="Portrait photo of Rhona Pellow"></div>
  <div class="avatar" style="left:886px" role="img" aria-label="Portrait photo of Tessa Marlowe"></div>
  <span class="dot" style="left:572px"></span><span class="dot" style="left:594px"></span><span class="dot on" style="left:618px"></span>
</section>

<section class="blogs">
  <h2 class="heading">LATEST BLOGS</h2>
  <article class="blog-card" style="left:125px">
    <div class="blog-img" role="img" aria-label="Photo of a glowing circuit board with SEO icons" style="background:linear-gradient(135deg,#0a1f3a,#1d6f9e 60%,#0c2742)"></div>
    <h4>Lorem ipsum dolor sit amet, consectetur adipiscing elit, sed do</h4>
    <p>Lorem ipsum dolor sit amet, consectetur adipiscing elit, sed do eiusmod tempor</p>
    <div class="btn-outline">LEARN MORE</div>
  </article>
  <article class="blog-card" style="left:450px">
    <div class="blog-img" role="img" aria-label="Photo of a hand holding a pen beside an SEO search bar" style="background:linear-gradient(135deg,#3c4a4f,#9aa7a6 55%,#c9a388)"></div>
    <h4>Lorem ipsum dolor sit amet, consectetur adipiscing elit, sed do</h4>
    <p>Lorem ipsum dolor sit amet, consectetur adipiscing elit, sed do eiusmod tempor</p>
    <div class="btn-outline">LEARN MORE</div>
  </article>
  <article class="blog-card" style="left:776px">
    <div class="blog-img" role="img" aria-label="Photo of hands on a tablet with floating SEO icons" style="background:linear-gradient(135deg,#b9c7de,#5b7bb3 55%,#2e4a86)"></div>
    <h4>Lorem ipsum dolor sit amet, consectetur adipiscing elit, sed do</h4>
    <p>Lorem ipsum dolor sit amet, consectetur adipiscing elit, sed do eiusmod tempor</p>
    <div class="btn-outline">LEARN MORE</div>
  </article>
  <svg class="abs" style="left:0;top:560px" width="1200" height="90" viewBox="0 0 1200 90"><polygon points="0,40 1000,90 1200,30 1200,90 0,90" fill="#fff"/></svg>
</section>

<section class="faq">
  <h2 class="heading">FREQUENTLY ASKED QUESTIONS</h2>
  <div class="faq-open">
    <h4>Lorem ipsum dolor sit amet, consectetur adipiscing elit ?</h4>
    <p>Sed ut perspiciatis unde omnis iste natus error sit voluptatem accusantium doloremque laudantium, totam rem aperiam, eaque ipsa quae ab illo inventore veritatis et quasi architecto beatae vitae dicta sunt explicabo. Nemo enim ipsam voluptatem quia voluptas sit aspernatur aut odit aut fugit, sed quia consequuntur magni dolores eos</p>
    <svg class="abs chev" style="right:16px;top:14px" viewBox="0 0 24 24" fill="none" stroke="#fff" stroke-width="1.5"><circle cx="12" cy="12" r="10"/><path d="M8 14l4-4 4 4"/></svg>
  </div>
  <div class="faq-item" style="top:3508px">Sed ut perspiciatis unde omnis iste natus ?<svg class="chev" viewBox="0 0 24 24" fill="none" stroke="#5b8fe0" stroke-width="1.5"><circle cx="12" cy="12" r="10"/><path d="M8 10l4 4 4-4"/></svg></div>
  <div class="faq-item" style="top:3567px">Error sit voluptatem accusantium doloremque laudantium ?<svg class="chev" viewBox="0 0 24 24" fill="none" stroke="#5b8fe0" stroke-width="1.5"><circle cx="12" cy="12" r="10"/><path d="M8 10l4 4 4-4"/></svg></div>
  <div class="faq-item" style="top:3627px">Totam rem aperiam, eaque ipsa quae ab illo inventore ?<svg class="chev" viewBox="0 0 24 24" fill="none" stroke="#5b8fe0" stroke-width="1.5"><circle cx="12" cy="12" r="10"/><path d="M8 10l4 4 4-4"/></svg></div>
  <div class="faq-item" style="top:3688px">Veritatis et quasi architecto beatae vitae dicta ?<svg class="chev" viewBox="0 0 24 24" fill="none" stroke="#5b8fe0" stroke-width="1.5"><circle cx="12" cy="12" r="10"/><path d="M8 10l4 4 4-4"/></svg></div>
</section>

<section class="contact">
  <svg class="notch" width="1200" height="130" viewBox="0 0 1200 130"><polygon points="0,0 1200,0 1200,20 600,128 0,20" fill="#fff"/></svg>
  <h2 class="heading">FILL OUR CONTACT FORM</h2>
  <div class="field" style="left:183px;top:250px;width:407px">First Name<i>*</i></div>
  <div class="field" style="left:601px;top:250px;width:408px">Last Name<i>*</i></div>
  <div class="field" style="left:183px;top:319px;width:407px">Contact Number<i>*</i></div>
  <div class="field" style="left:601px;top:319px;width:408px">E-mail<i>*</i></div>
  <div class="field msg" style="left:188px;top:388px;width:825px;height:127px">Leave a Message</div>
  <div class="btn-send">SEND MESSAGE</div>
</section>

<footer class="site-footer">
  <div class="brand">linkora</div>
  <div class="f-col" style="left:140px"><h5>INFORMATION</h5><ul><li>Home</li><li>About Us</li><li>Services</li><li>News &amp; Blogs</li><li>Contact</li></ul></div>
  <div class="f-col" style="left:355px"><h5>LINKS</h5><ul><li>Careers</li><li>Support</li><li>Sitemap</li><li>Privacy Policy</li><li>Contact Us</li></ul></div>
  <div class="f-col" style="left:545px"><h5>CONTACT US</h5>
    <div class="c-row"><svg width="26" height="28" viewBox="0 0 26 28" fill="none" stroke="#fff" stroke-width="1.6"><path d="M13 22s-7-7-7-12a7 7 0 0114 0c0 5-7 12-7 12z"/><circle cx="13" cy="10" r="2.5"/><ellipse cx="13" cy="24" rx="10" ry="3"/></svg><div><b>ADDRESS</b><span>418 Larkfield Lane Ashbourne</span></div></div>
    <div class="c-row"><svg width="26" height="26" viewBox="0 0 26 26" fill="none" stroke="#fff" stroke-width="1.6"><path d="M6 3l4 1 1 5-3 2a13 13 0 007 7l2-3 5 1 1 4c-1 2-3 3-5 3C9 23 3 17 3 9c0-2 1-5 3-6z"/></svg><div><b>PHONE</b><span>(555)-014-7730</span></div></div>
    <div class="c-row"><svg width="26" height="22" viewBox="0 0 26 22" fill="none" stroke="#fff" stroke-width="1.6"><rect x="2" y="3" width="22" height="16"/><path d="M2 3l11 9 11-9"/></svg><div><b>EMAIL US</b><span>hello@linkora.example</span></div></div>
  </div>
  <div class="f-col" style="left:848px;top:124px"><h5>NEWSLETTER</h5>
    <div class="news-input">Your E-mail<span class="news-go"><svg width="12" height="12" viewBox="0 0 12 12" fill="none" stroke="#fff" stroke-width="1.8"><path d="M1 6h9M6 2l4 4-4 4"/></svg></span></div>
    <div class="socials"><span></span><span></span><span></span><span></span><span></span></div>
  </div>
  <div class="copy">Copyright © 2021 Linkora<br>All Right Reserved</div>
</footer>

</body>
</html>
```